Dale Morrikan Plumbing and Heating

Need a card design for a plumbing and heating company that does service and repair, remodels, and plumbing in new construction. Please add following on back side of card; Boilers, Water heaters, Gas lines, Sump pumps, Toilet repairs, Faucet repairs, Pipe thawing, Radiant heating, New construction, Remodels.

Industry/Entity Type

Plumber

Contact Information for Business Card

Was thinking white gloss card with colored logo in middle or black glossy card with silver logo in middle. Just a thought but very open to other designs.

Requirements
Must have
• Need following on front of card;
• P(203) 321-8689
• C(203) 232-9069
• Dale Morrikan 275 Larkwell St West, Alderbrook, Md 06214
• service@DrainHearth.example (plumbing in blue, heating in red)
• www.DrainHearth.example (plumbing in blue, heating in red)
• Fully Licensed and Insured
Nice to have
• Elegant design

```html
<!DOCTYPE html>
<html lang="en">
<head>
<meta charset="utf-8">
<title>Dale Morrikan Plumbing and Heating – Business Card</title>
<link rel="stylesheet" href="https://fonts.googleapis.com/css2?family=Open+Sans:ital,wght@0,400;0,600;0,700;1,400&display=swap">
<style>
  :root {
    --stage: #e9ebef;
    --royal: #3a3fb8;
    --royal-deep: #2b2f9a;
    --sky: #2f86d8;
    --sky-light: #5aa6e6;
    --navy: #2b3a9c;
    --accent-red: #d8343c;
    --band-red: #c8404a;
    --band-grey: #b8bcc4;
    --paper: #ffffff;
    --ink-white: #ffffff;
    --ink-grey: #6b6f78;
  }
  * { box-sizing: border-box; margin: 0; padding: 0; }
  html, body { width: 1200px; height: 851px; overflow: hidden; }
  body {
    background: var(--stage);
    font-family: "Open Sans", Arial, sans-serif;
    display: flex;
    align-items: center;
    justify-content: center;
    gap: 40px;
  }
  .card {
    position: relative;
    width: 530px;
    height: 303px;
    border-radius: 16px;
    overflow: hidden;
    box-shadow: 0 10px 26px rgba(0,0,0,.18);
  }

  /* Back side */
  .card-back {
    background: radial-gradient(ellipse at 50% 55%, var(--sky) 0%, var(--royal) 60%, var(--royal-deep) 100%);
    color: var(--ink-white);
    text-align: center;
  }
  .back-mark {
    position: absolute;
    top: 70px; left: 0; right: 0;
    display: flex; align-items: center; justify-content: center; gap: 10px;
    font-weight: 700; font-size: 26px; letter-spacing: .5px;
  }
  .mark-dot { width: 14px; height: 14px; border-radius: 50%; background: var(--ink-white); }
  .back-claim {
    position: absolute; top: 152px; left: 0; right: 0;
    font-weight: 700; font-size: 20px;
  }
  .service-list {
    position: absolute; top: 190px; left: 40px; right: 40px;
    font-size: 12.5px; line-height: 1.7;
  }
  .service-list .sep {
    display: inline-block; width: 6px; height: 6px; border-radius: 50%;
    background: var(--ink-white); margin: 0 6px; vertical-align: middle;
  }

  /* Front side */
  .card-front { background: var(--paper); }
  .front-wave { position: absolute; inset: 0; }
  .holder { position: absolute; top: 44px; left: 34px; }
  .holder-name { color: var(--navy); font-weight: 600; font-size: 22px; line-height: 1.1; }
  .holder-role { color: var(--accent-red); font-size: 15px; }
  .brand {
    position: absolute; top: 30px; right: 30px; text-align: right;
  }
  .brand-name {
    display: flex; align-items: center; justify-content: flex-end; gap: 8px;
    color: var(--navy); font-weight: 700; font-size: 17px; line-height: 1.2;
  }
  .brand-name .mark-dot { background: var(--navy); width: 12px; height: 12px; }
  .brand-web {
    margin-top: 6px; padding-top: 4px; border-top: 1px solid var(--band-grey);
    color: var(--ink-grey); font-size: 10px;
  }
  .address {
    position: absolute; top: 160px; right: 30px;
    color: var(--ink-white); font-size: 13px; line-height: 1.5; text-align: right;
  }
  .contact {
    position: absolute; bottom: 26px; left: 34px;
    color: var(--ink-white); font-size: 13.5px; line-height: 1.55;
  }
  .contact b { font-weight: 700; }
</style>
</head>
<body>

  <section class="card card-back" aria-label="Card back">
    <div class="back-mark"><span class="mark-dot"></span>Dale Morrikan</div>
    <p class="back-claim">Fully Licensed and Insured</p>
    <p class="service-list">
      Boilers<span class="sep"></span>Water heaters<span class="sep"></span>Gas lines<span class="sep"></span>Sump pumps<span class="sep"></span>Toilet repairs<br>
      Faucet repairs<span class="sep"></span>Pipe thawing<span class="sep"></span>Radiant heating<br>
      New construction<span class="sep"></span>Remodels.
    </p>
  </section>

  <section class="card card-front" aria-label="Card front">
    <svg class="front-wave" viewBox="0 0 530 303" preserveAspectRatio="none" aria-hidden="true">
      <defs>
        <linearGradient id="frontBlue" x1="0" y1="0" x2="1" y2="1">
          <stop offset="0" stop-color="#5aa6e6"/>
          <stop offset=".55" stop-color="#2f86d8"/>
          <stop offset="1" stop-color="#2b56c4"/>
        </linearGradient>
      </defs>
      <path d="M0,172 C130,208 280,214 530,116 L530,303 L0,303 Z" fill="#c8404a"/>
      <path d="M0,180 C130,216 280,222 530,124 L530,303 L0,303 Z" fill="#b8bcc4"/>
      <path d="M0,193 C140,228 290,230 530,132 L530,303 L0,303 Z" fill="url(#frontBlue)"/>
    </svg>

    <div class="holder">
      <p class="holder-name">Evan Holt</p>
      <p class="holder-role">CEO/Founder</p>
    </div>

    <div class="brand">
      <p class="brand-name"><span class="mark-dot"></span>Dale Morrikan<br>Plumbing and Heating</p>
      <p class="brand-web">www.DrainHearth.example</p>
    </div>

    <p class="address">Dale Morrikan<br>275 Larkwell St West<br>Alderbrook, Md 06214</p>

    <p class="contact">
      <b>Phone:</b> (410) 555-0147<br>
      <b>Mobile:</b> (410) 555-0183<br>
      service@DrainHearth.example
    </p>
  </section>

</body>
</html>
```